Valdarossi’s Artisan Pizzeria Menu Contest

I’m looking for a menu design for a new pizzeria - it’s farm to table type of restaurant - more upscale than a typical pizzeria - white washed wood interior with some industrial accents - I am looking for a creative menu layout using the attached sample menu items -
Valdarossi’s is an artisanal pizzeria with an atmosphere that will make you feel at home for any situation, first date, anniversary, business lunch, boys night out or girls night out with a menu inspired by the idea of a simple honest cooking paired with fresh – quality ingredients. Full service dining experience that is still casual but dedicated to extraordinary hospitality.
While developing the menu we have created a network of amazing farms and purveyors to supply our restaurant with fresh milled 100% California flour for our hand crafted dough, as well as sustainably farmed organic produce, meats and cheeses.
The menu includes classics like the Margherita pizza to daily seasonal specials, fresh salads to rustic small plates including moms meatball recipe to a fresh local burrata with handmade bread. Each dish reflects our passion for sourcing the freshest quality local ingredients.
To compliment the menu, Valdarossi’s serves an extensive wine list with selections focusing on Italian varietals. The cocktail program has been carefully crafted to offer something to entice ever palate and the beer list has unique selections of the world’s finest brewers.
Target Market(s)
25-45 year old men and women
Industry/Entity Type
American Restaurant
Requirements
Must have
- professional tone
Nice to have
- a balance of elegance and industrial (rustic)
Should not have
- photos or playful graphics etc..

```html
<!DOCTYPE html>
<html lang="en">
<head>
<meta charset="utf-8">
<title>Valdarossi’s Artisan Pizzeria Menu</title>
<link href="https://fonts.googleapis.com/css2?family=Montserrat:ital,wght@0,400;0,500;0,600;1,400&display=swap" rel="stylesheet">
<style>
  :root {
    --ink: #111111;
    --frame: #0d0d0d;
    --paper: #ffffff;
    --accent: #e8463f;
    --muted: #6a6a6a;
  }
  * { margin: 0; padding: 0; box-sizing: border-box; }
  html, body { width: 969px; height: 1200px; overflow: hidden; background: var(--paper); }
  body { font-family: "Montserrat", Arial, sans-serif; color: var(--ink); }

  .menu { position: relative; width: 969px; height: 1200px; }
  .menu__frame { position: absolute; inset: 0; background: var(--frame); }
  .menu__sheet { position: absolute; left: 50px; top: 50px; width: 870px; height: 1100px; background: var(--paper); }

  .brand {
    position: absolute; left: 0; top: 0; width: 969px; text-align: center;
    top: 145px; font-size: 40px; font-weight: 600; letter-spacing: 1px; color: var(--ink);
  }

  .rule { position: absolute; width: 2px; background: var(--accent); }

  .heading {
    position: absolute; text-align: center; font-size: 26px; font-weight: 400;
    letter-spacing: 0.3px; line-height: 1; transform: translateX(-50%);
    white-space: nowrap;
  }
  .heading__title { display: inline-block; padding: 0 4px 6px; border-bottom: 2px solid var(--accent); position: relative; }
  .heading__title::after {
    content: ""; position: absolute; left: 12%; right: 12%; bottom: -7px; height: 2px; background: var(--accent);
  }
  .heading__mark {
    display: inline-block; width: 8px; height: 8px; border: 2px solid var(--accent);
    transform: rotate(45deg); vertical-align: 6px; margin: 0 4px;
  }

  .section { position: absolute; }
  .item { height: var(--step); }
  .item__row { display: flex; justify-content: space-between; font-size: 12.5px; font-weight: 500; text-transform: uppercase; line-height: 1.15; }
  .item__price { white-space: nowrap; }
  .item__desc { margin-top: 3px; font-size: 8.4px; font-style: italic; color: var(--muted); line-height: 1.25; max-width: 270px; }
</style>
</head>
<body>
<main class="menu">
  <div class="menu__frame" role="img" aria-label="Black border with a repeating white diamond pattern"></div>
  <div class="menu__sheet"></div>

  <div class="brand">Valdarossi’s</div>

  <div class="rule" style="left:327px;top:249px;height:842px"></div>
  <div class="rule" style="left:337px;top:256px;height:856px"></div>
  <div class="rule" style="left:631px;top:249px;height:862px"></div>
  <div class="rule" style="left:641px;top:256px;height:856px"></div>

  <!-- Appetizers -->
  <h2 class="heading" style="left:180px;top:329px"><span class="heading__mark"></span><span class="heading__title">APPETIZERS</span><span class="heading__mark"></span></h2>
  <section class="section" style="left:70px;top:389px;width:246px;--step:44px">
    <div class="item"><div class="item__row"><span>Brussels</span><span class="item__price">$ 10.00</span></div><p class="item__desc">Pan seared brussel sprouts with a drizzle of balsamic reduction and parm and bread crumbs</p></div>
    <div class="item"><div class="item__row"><span>Meatballs</span><span class="item__price">$ 13.00</span></div><p class="item__desc">Moms meatballs handmade secret recipe for over 75 years</p></div>
    <div class="item"><div class="item__row"><span>Mussels</span><span class="item__price">$ 15.00</span></div><p class="item__desc" style="margin-top:10px">New Zealand Mussels in a tomato broth</p></div>
    <div class="item"><div class="item__row"><span>Romanesco</span><span class="item__price">$ 11.00</span></div><p class="item__desc" style="margin-top:10px">Flash fried romanesco served atop a spicy aioli</p></div>
    <div class="item"><div class="item__row"><span>Chicken Wings</span><span class="item__price">$ 10.00</span></div><p class="item__desc" style="margin-top:10px">Italian fried chicken wings with a kick</p></div>
    <div class="item"><div class="item__row"><span>Burrata</span><span class="item__price">$ 13.00</span></div><p class="item__desc">Local burrata served with apples grapes and fresh made bread</p></div>
  </section>

  <!-- Salads -->
  <h2 class="heading" style="left:170px;top:732px"><span class="heading__mark"></span><span class="heading__title">SALADS</span><span class="heading__mark"></span></h2>
  <section class="section" style="left:72px;top:792px;width:233px;--step:47.5px">
    <div class="item"><div class="item__row"><span>Chopped Salad</span><span class="item__price">$ 13.00</span></div><p class="item__desc">Lettuce mix with tomato, onions, peppers, pepperoni, chick peas, fresh mozz, italian herb ving</p></div>
    <div class="item"><div class="item__row"><span>Caesar Salad</span><span class="item__price">$ 11.00</span></div><p class="item__desc">Traditional caesar salad rich and creamy extra shaved parmesan</p></div>
    <div class="item"><div class="item__row"><span>Farm Salad</span><span class="item__price">$ 15.00</span></div><p class="item__desc">Seasonal farmers market salad</p></div>
    <div class="item"><div class="item__row"><span>Grilled Little Gem</span><span class="item__price">$ 11.00</span></div><p class="item__desc">Grilled little gems with bacon, tomato, red onions and blue cheese dressing</p></div>
    <div class="item"><div class="item__row"><span>Spinach and Arugula<br>Salad</span><span class="item__price">$ 12.00</span></div><p class="item__desc" style="margin-top:7px">Spinach and argula, red pepperstossed in a lemon ving and housemade croutons</p></div>
  </section>

  <!-- Pizzas -->
  <h2 class="heading" style="left:485px;top:352px"><span class="heading__mark"></span><span class="heading__title">PIZZAS</span><span class="heading__mark"></span></h2>
  <section class="section" style="left:350px;top:412px;width:269px;--step:45.4px">
    <div class="item"><div class="item__row"><span>Margherita</span><span class="item__price">$ 14.00</span></div><p class="item__desc">Classic Margherita pizza - Fresh Mozz Tomato Sauce and Basil</p></div>
    <div class="item"><div class="item__row"><span>Organic Sausage</span><span class="item__price">$ 16.00</span></div><p class="item__desc">Housemade Red Sauce Mozz hint of fennel</p></div>
    <div class="item"><div class="item__row"><span>Pepperoni</span><span class="item__price">$ 16.00</span></div><p class="item__desc">Calder Pepperoni Housemade Red Sauce Chile flakes and Mozz</p></div>
    <div class="item"><div class="item__row"><span>Salumi and Burrata</span><span class="item__price">$ 17.00</span></div><p class="item__desc">Salumi dried Red Sauce finished with whipped burrata</p></div>
    <div class="item"><div class="item__row"><span>Daily Special</span><span class="item__price">$ 17.00</span></div></div>
    <div class="item"><div class="item__row"><span>Mushroom</span><span class="item__price">$ 15.00</span></div><p class="item__desc">Shaved mushrooms with a Parmesan cream and melted onions</p></div>
    <div class="item"><div class="item__row"><span>Prosciutto and Egg</span><span class="item__price">$ 16.00</span></div><p class="item__desc" style="margin-top:1px">Prosciutto Parmesan cream with Alpine and gruyere finished with an organic egg</p></div>
    <div class="item"><div class="item__row"><span>Quarttro Formaggi</span><span class="item__price">$ 15.00</span></div><p class="item__desc" style="margin-top:1px">Four cheese combination mozz - fontina - parm cream and gruyere chile flakes and oregano</p></div>
    <div class="item"><div class="item__row"><span>Farmers Pizza</span><span class="item__price">$ 17.00</span></div><p class="item__desc">Seasonal vegatables cream sauce and a variety of cheese</p></div>
    <div class="item"><div class="item__row"><span>Keto Friendly</span><span class="item__price">$ 17.00</span></div><p class="item__desc" style="margin-top:6px">Cauliflower crust, spinach and kale , parm cream sauce</p></div>
  </section>

  <!-- Daily soup -->
  <h2 class="heading" style="left:477px;top:950px"><span class="heading__mark"></span><span class="heading__title">DAILY SOUP</span><span class="heading__mark"></span></h2>
  <section class="section" style="left:350px;top:1010px;width:269px;--step:40px">
    <div class="item"><div class="item__row"><span>Example Tomato<br>Bisque</span><span class="item__price">$ 8.00</span></div></div>
  </section>

  <!-- Sandwiches -->
  <h2 class="heading" style="left:779px;top:329px"><span class="heading__mark"></span><span class="heading__title">SANDWICHES</span><span class="heading__mark"></span></h2>
  <section class="section" style="left:653px;top:391px;width:245px;--step:53.2px">
    <div class="item"><div class="item__row"><span>Italian Sub</span><span class="item__price">$ 13.00</span></div><p class="item__desc" style="margin-top:6px">Prociutto, salumi, turkey, provolone, lettuce, tomato and herb aioli with spicy gardenia</p></div>
    <div class="item"><div class="item__row"><span>Turkey Sandwich</span><span class="item__price">$ 12.00</span></div><p class="item__desc" style="margin-top:6px">housemade bread - turkey, cheddar cheese, butter lettuce, omato and mustard aioli</p></div>
    <div class="item"><div class="item__row"><span>Meatball Sub</span><span class="item__price">$ 13.00</span></div><p class="item__desc" style="margin-top:9px">Moms meatballs melted provolone on a housemade roll</p></div>
    <div class="item"><div class="item__row"><span>Plantwise Burger</span><span class="item__price">$ 14.00</span></div><p class="item__desc" style="margin-top:6px">Housemade bun - arugula , tomato, onion and a sundried tomato spread</p></div>
    <div class="item"><div class="item__row"><span>Chicken Sandwich</span><span class="item__price">$ 13.00</span></div><p class="item__desc" style="margin-top:6px">Fried chicken or chicken breast, provolone, argula, tomato, served with a spicy aioli</p></div>
  </section>

  <!-- Crusts -->
  <h2 class="heading" style="left:777px;top:700px"><span class="heading__mark"></span><span class="heading__title">CRUSTS</span><span class="heading__mark"></span></h2>
  <section class="section" style="left:654px;top:757px;width:245px;--step:31.8px">
    <div class="item"><div class="item__row"><span>Traditional</span><span class="item__price">$ 3.00</span></div><p class="item__desc" style="margin-top:2px">Orginal crust you can't miss</p></div>
    <div class="item"><div class="item__row"><span>Gluten Free</span><span class="item__price">$ 3.00</span></div><p class="item__desc" style="margin-top:2px">Best gluten friendly crust on the west coast</p></div>
    <div class="item"><div class="item__row"><span>Cauliflower</span><span class="item__price">$ 3.00</span></div><p class="item__desc" style="margin-top:3px">Vegans have needs</p></div>
  </section>

  <!-- Dips -->
  <h2 class="heading" style="left:776px;top:900px"><span class="heading__mark"></span><span class="heading__title">DIPS</span><span class="heading__mark"></span></h2>
  <section class="section" style="left:654px;top:955px;width:245px;--step:24px">
    <div class="item"><div class="item__row"><span>Ranch</span><span class="item__price">$ 1.00</span></div></div>
    <div class="item"><div class="item__row"><span>Tomato Sauce</span><span class="item__price">$ 1.00</span></div></div>
    <div class="item"><div class="item__row"><span>Spicy Dip</span><span class="item__price">$ 1.00</span></div></div>
    <div class="item"><div class="item__row"><span>Blue Cheese</span><span class="item__price">$ 1.00</span></div></div>
  </section>
</main>
</body>
</html>
```